Homepage design competition to choose a designer for $1500 full website for a Small Animal Veterinar

We are running a homepage design competition to choose a designer who will later code an entire website. Please note, this competition is only for the front page design. There will be an additional payment of $1500 (Australian $AUD) for the complete website design including coding payment.

Front Page: First we need a front page design for our companion animal veterinary hospital. I will use the frontpage design competition to choose a designer for the full website.
Marlow Vet Clinic is a companion animal veterinary hospital in Singleton NSW. We provide veterinary medical and surgical treatment for dogs, cats, rabbits, birds and reptiles. Mostly dogs and cats.
Our reception is a 120 year old church and the hospital is 6 years old and custom built.
I want the site to be amazing. The sort of thing that could win prizes. The front page should be simple, fun and engaging whilst maintaining a strong sense of professionalism. Simple and elegant visual effects with subtle movement. The winning design will show originality.
Our main demographic is women aged 25 to 44 years old. We are a coal mining town. Most of our money comes from coal miners wives.
The front page must display our phone number and link to our facebook page. Otherwise the front page can have anything. The front page should impress new clients and reassure existing clients.
We pride ourselves on following up everything and caring for pets and their people their entire life. Please see our existing (horrible) website for more details about our business. http://www.marlowvetclinic.example/
Incorporate only amazing things from the old website. I hate the old website, so there is probably not much to use. We need something new and amazing.
Fully responsive design.

Characters: We have a logo and animal characters to incorporate into the design. These characters will be used throughout our email and facebook advertising. If they could be used with some movement and sound effects, that would be cool, but nothing too childish or silly.

Live site: please include links to live demo sites if possible.
Please include links to your other work.

Full Website: The successful designer of the frontpage must be able to demonstrate the ability produce a full website. The full website designer will be commissioned after the front page is chosen. We have budgeted for a full website of $1500.
I need to be able to add new articles to the website that will link from email newsletters and facebook, so the full website will need to be something I can modify or add to.
I have a working knowledge of Joomla, Wordpress and html.
The full website will have map, history of the hospital, history of the chapel, links to local services, pet care advice, memorials.
Ideally the winning designer will be able to integrate appointments available with our existing veterinary management software.
Fully responsive design.

Here are some websites that I like:
https://drbexley.example.au/
http://quincepepper.example/
http://www.xn--dorotawelnicka-abc12k.example/
https://www.zov.example.au/
https://www.frisko.example.au/
https://topmowers.example.au/
https://www.redgatecider.example/

Target Market(s)

Women aged 25 to 44 years

Industry/Entity Type

Veterinary

Number of Pages Required

1 page

Font styles to use
Serif
Sans Serif

Requirements
Must have
• Phone number
• Facebook Link https://www.facebook.com/marlow.vetclinic?v=wall
• Simplicity
• Originality
• Animal characters-images attached
Nice to have
• Images
• Clean
• Link to live site.
• Links to your other work.
• Demonstrate ability to integrate appointment booking with our veterinary software
Should not have
• Heaps of words
• Complexity

```html
<!DOCTYPE html>
<html lang="en">
<head>
<meta charset="utf-8">
<title>Marlow Vet Clinic</title>
<link rel="stylesheet" href="https://fonts.googleapis.com/css2?family=Quicksand:wght@400;500;600;700&display=swap">
<style>
:root{
  --green:#8dc03f;
  --orange:#e97c3a;
  --orange-soft:#f58d4e;
  --terracotta:#d4825a;
  --brown:#a6836a;
  --brown-dark:#4f2f1d;
  --brown-deep:#3f2416;
  --text:#3a3a3a;
  --muted:#777;
  --sky-top:#84c8ee;
  --sky-low:#cfeaf8;
  --grass:#7fb23a;
  --ground:#ececec;
  --white:#fff;
}
*{box-sizing:border-box;margin:0;padding:0}
html,body{width:1119px;height:1200px;overflow:hidden}
body{position:relative;font-family:"Quicksand",sans-serif;color:var(--text);
  background:linear-gradient(to bottom,var(--sky-top) 0,var(--sky-low) 280px,#b9dc7a 300px,var(--grass) 340px,#5f9a2a 398px,#e4e4e4 400px,var(--ground) 1005px,var(--brown-dark) 1005px)}
.abs{position:absolute}
/* header */
.header-strip{left:140px;top:25px;width:22px;height:50px;background:var(--green)}
.nav-bar{left:333px;top:25px;width:646px;height:50px;background:var(--green);display:flex;align-items:center}
.nav{display:flex;gap:0;margin-left:49px}
.nav a{color:var(--white);text-decoration:none;font-weight:700;font-size:12.5px;letter-spacing:.4px;margin-right:34px}
.social{margin-left:auto;margin-right:22px;display:flex;gap:7px}
.social span{width:8px;height:8px;border-radius:50%;background:var(--white);display:block}
.panel{left:140px;top:75px;width:839px;height:365px;background:var(--white)}
.logo-box{left:162px;top:25px;width:171px;height:115px;background:var(--white);display:flex;flex-direction:column;align-items:center;justify-content:center;gap:8px}
.logo-box .dot{width:26px;height:26px;border-radius:50%;background:var(--green)}
.logo-box .name{font-weight:700;font-size:17px;color:var(--brown-dark);text-align:center;line-height:1.1}
.frog{left:70px;top:178px;width:140px;height:140px;border-radius:40% 50% 45% 50%;background:radial-gradient(circle at 55% 45%,#9fd05a,#78b236 70%,rgba(120,178,54,0) 72%)}
.hero-photo{left:590px;top:75px;width:389px;height:365px;background:linear-gradient(160deg,#f4f1ee 0,#e9dcd0 30%,#9cc6e4 60%,#c9a27a 100%)}
.welcome{left:220px;top:170px;width:380px}
.welcome h1{font-size:24.5px;font-weight:700;color:var(--green);letter-spacing:.5px;margin-bottom:8px}
.welcome p{font-size:10.5px;line-height:12.8px;color:var(--text);width:340px}
.welcome h3{font-size:10.5px;font-weight:700;margin:17px 0 4px}
.ticks{list-style:none}
.ticks li{font-size:10.5px;line-height:17px;padding-left:23px;position:relative}
.ticks li svg{position:absolute;left:8px;top:4px}
.hours{left:220px;top:362px}
.hours h4{font-size:13px;font-weight:600;color:var(--orange);margin-bottom:6px}
.hours p{font-size:10.5px;line-height:13px;color:var(--orange)}
/* contact band */
.contact{left:140px;top:440px;width:295px;height:135px;background:var(--orange);color:var(--white);padding:33px 0 0 39px}
.contact .row{display:flex;gap:9px;align-items:center}
.contact .lbl{font-size:11.5px;font-weight:700;line-height:12px}
.contact .num{font-size:20px;font-weight:700;letter-spacing:.5px}
.contact .addr{font-size:10px;font-weight:700;line-height:13.5px;margin-top:16px}
.testimonial{left:435px;top:440px;width:544px;height:135px;background:var(--brown);color:var(--white);padding:34px 34px 0 35px}
.testimonial p{font-size:9.2px;line-height:11.6px}
.dots{display:flex;gap:6px;justify-content:center;margin-top:12px;margin-left:-90px}
.dots span{width:8px;height:8px;border-radius:50%;background:#7a5a43}
.dots span:first-child{background:var(--white)}
/* service cards */
.card{width:192px;height:128px;background:var(--white);text-align:center;border-top:10px solid var(--c)}
.card .icon{position:absolute;left:68px;top:-37px;width:55px;height:55px;border-radius:50%;background:var(--c);display:flex;align-items:center;justify-content:center}
.card h2{font-size:12.5px;font-weight:600;color:#555;letter-spacing:.4px;margin-top:45px}
.card p{font-size:9.3px;line-height:12px;color:var(--muted);margin:13px auto 0;width:150px}
/* footer */
.tab{left:140px;top:987px;width:125px;height:36px;background:var(--orange);color:var(--white);font-size:12px;font-weight:700;display:flex;align-items:center;justify-content:center;letter-spacing:.3px}
.tab::after{content:"";position:absolute;right:-8px;top:0;border-left:8px solid var(--orange);border-bottom:18px solid transparent}
.field{top:1046px;width:207px;height:55px;background:#f1f1f1;border:none;font-family:inherit;font-size:8px;color:#444;padding:9px 14px;resize:none}
.submit{left:140px;top:1108px;width:59px;height:23px;background:var(--green);color:var(--white);border:none;font-family:inherit;font-weight:700;font-size:9px}
.site-nav{left:605px;top:1040px;color:var(--white)}
.site-nav h5{font-size:11.5px;font-weight:600;margin-bottom:8px}
.site-nav .cols{display:flex;gap:23px}
.site-nav a{display:block;color:var(--white);text-decoration:none;font-size:8px;line-height:12.6px}
.duck{left:770px;top:985px;width:195px;height:160px;border-radius:50% 45% 40% 50%;background:radial-gradient(ellipse at 55% 45%,#a57a5c,#8a6148 60%,rgba(138,97,72,0) 72%)}
.rule{left:0;top:1155px;width:1119px;height:2px;background:var(--brown-deep)}
.bottom{top:1157px;left:0;width:1119px;height:43px;background:var(--brown-dark);color:#b79a85}
.bottom .phone{position:absolute;left:140px;top:11px;display:flex;gap:5px;align-items:center;font-size:15px;font-weight:700}
.bottom .social{position:absolute;left:529px;top:17px;margin:0;gap:10px}
.bottom .social span{background:#b79a85;width:10px;height:10px}
.bottom .copy{position:absolute;right:140px;top:16px;font-size:7.5px}
</style>
</head>
<body>
<div class="abs header-strip"></div>
<div class="abs panel"></div>
<div class="abs nav-bar">
  <nav class="nav"><a href="#">Home</a><a href="#">Services</a><a href="#">Staff</a><a href="#">Contact</a><a href="#">Map</a><a href="#">History</a></nav>
  <div class="social"><span></span><span></span><span></span><span></span></div>
</div>
<div class="abs logo-box"><span class="dot"></span><span class="name">Marlow Vet Clinic</span></div>
<div class="abs frog" role="img" aria-label="Green frog character illustration"></div>
<div class="abs hero-photo" role="img" aria-label="Photo of a vet with a stethoscope holding a pug"></div>

<section class="abs welcome">
  <h1>Welcome Pet Lovers!</h1>
  <p>Marlow Vet Clinic is a Companion Animal Veterinary Hospital in Singleton committed to providing excellent care for loved pets and their owners.</p>
  <h3>To achieve this we:</h3>
  <ul class="ticks">
    <li><svg width="10" height="9" viewBox="0 0 10 9"><rect x=".5" y="1.5" width="7" height="7" fill="none" stroke="#333"/><path d="M2 4.5l2 2L9.5 .5" fill="none" stroke="#333" stroke-width="1.4"/></svg>Provide a welcoming environment.</li>
    <li><svg width="10" height="9" viewBox="0 0 10 9"><rect x=".5" y="1.5" width="7" height="7" fill="none" stroke="#333"/><path d="M2 4.5l2 2L9.5 .5" fill="none" stroke="#333" stroke-width="1.4"/></svg>Treat all patients and owners as important.</li>
    <li><svg width="10" height="9" viewBox="0 0 10 9"><rect x=".5" y="1.5" width="7" height="7" fill="none" stroke="#333"/><path d="M2 4.5l2 2L9.5 .5" fill="none" stroke="#333" stroke-width="1.4"/></svg>Educate owners to help prevent illness.</li>
    <li><svg width="10" height="9" viewBox="0 0 10 9"><rect x=".5" y="1.5" width="7" height="7" fill="none" stroke="#333"/><path d="M2 4.5l2 2L9.5 .5" fill="none" stroke="#333" stroke-width="1.4"/></svg>When illness occurs, treat with the latest equipment and techniques.</li>
  </ul>
</section>
<section class="abs hours">
  <h4>Regular Opening Hours</h4>
  <p>Monday to Friday - 8:30am to 5:30pm<br>Saturday - 9:00am to 12:00 midday</p>
</section>

<section class="abs contact">
  <div class="row">
    <svg width="29" height="29" viewBox="0 0 29 29"><rect width="29" height="29" rx="6" fill="#fff"/><path d="M9 7c1.5-1 2.5-.5 3 1l1 3c.3 1-.5 1.7-1.3 2.2.8 2 2.2 3.5 4.2 4.4.5-.8 1.2-1.6 2.2-1.3l3 1c1.5.5 2 1.5 1 3-1.5 2-3.5 2.5-6 1.2C11.5 19.5 9.5 17 8 13.5 7 11 7.5 8.5 9 7z" fill="#e97c3a"/></svg>
    <div><div class="lbl">Contact now:</div><div class="num">02 65550192</div></div>
  </div>
  <div class="addr">14 Wattle Cl Singleton Heights NSW 2330<br>e-mail: mail@marlowvet.example</div>
</section>
<section class="abs testimonial">
  <p>"I would just like to thank you all from the bottom of my heart for being so caring and compassionate towards me and my dogs. All of the dogs drag me thru the door to you guys instead of the other way around and it's always such a pleasure for us to come and visit. Because I am a emotional person and really, really love my muts, I have found that I get the emotional support from you guys that I have not received from my previous vets and for that I thank you all very much. Keep up the fabulous work!!"</p>
  <div class="dots"><span></span><span></span><span></span></div>
</section>

<article class="abs card" style="--c:var(--terracotta);left:149px;top:628px"><div class="icon"><svg width="24" height="24" viewBox="0 0 24 24" fill="none" stroke="#fff" stroke-width="1.6"><path d="M7 3v6a4 4 0 008 0V3M11 13v4a3 3 0 006 0v-2"/><circle cx="17" cy="13" r="2"/></svg></div><h2>Appointment</h2><p>Make an appointment to clear your schedule ahead.</p></article>
<article class="abs card" style="--c:var(--green);left:358px;top:628px"><div class="icon"><svg width="26" height="24" viewBox="0 0 26 24" fill="none" stroke="#fff" stroke-width="1.6"><ellipse cx="13" cy="13" rx="7" ry="8"/><path d="M6 8C3 6 2 10 4 13M20 8c3-2 4 2 2 5"/><circle cx="10.5" cy="11" r="1" fill="#fff"/><circle cx="15.5" cy="11" r="1" fill="#fff"/><ellipse cx="13" cy="16" rx="2" ry="1.3"/></svg></div><h2>Puppy School</h2><p>Enroll your beloved puppy to us to learn skills and talent.</p></article>
<article class="abs card" style="--c:var(--brown);left:568px;top:628px"><div class="icon"><svg width="28" height="20" viewBox="0 0 28 20" fill="none" stroke="#fff" stroke-width="1.6"><ellipse cx="14" cy="7" rx="12" ry="4"/><path d="M2 7v4c0 2.5 5.5 4.5 12 4.5S26 13.5 26 11V7"/></svg></div><h2>Pet Care</h2><p>Let us take care of your pet when you're on a journey.</p></article>
<article class="abs card" style="--c:var(--orange-soft);left:780px;top:628px"><div class="icon"><svg width="24" height="24" viewBox="0 0 24 24" fill="none" stroke="#fff" stroke-width="1.6"><path d="M5 20l3-3M8 17l9-13 3 2-9 13z"/><path d="M13 8l3 2M12 10l3 2"/></svg></div><h2>Local Services</h2><p>Check our groomers, parks good for dog walking near you.</p></article>

<article class="abs card" style="--c:var(--brown);left:149px;top:803px"><div class="icon"><svg width="24" height="24" viewBox="0 0 24 24" fill="none" stroke="#fff" stroke-width="1.6"><ellipse cx="12" cy="16" rx="5" ry="4"/><circle cx="6" cy="10" r="2"/><circle cx="10" cy="6" r="2"/><circle cx="14" cy="6" r="2"/><circle cx="18" cy="10" r="2"/></svg></div><h2>Summer</h2><p>Know more about those pesky pests on summers.</p></article>
<article class="abs card" style="--c:var(--orange-soft);left:358px;top:803px"><div class="icon"><svg width="24" height="24" viewBox="0 0 24 24" fill="none" stroke="#fff" stroke-width="1.6"><circle cx="10" cy="4" r="2"/><path d="M10 7v8M7 9h6M8 22l2-7 2 7"/><rect x="13" y="13" width="6" height="5"/></svg></div><h2>Positions Vacant</h2><p>Check curent vacant jobs in our local clinic</p></article>
<article class="abs card" style="--c:var(--green);left:568px;top:803px"><div class="icon"><svg width="24" height="24" viewBox="0 0 24 24" fill="none" stroke="#fff" stroke-width="1.6"><path d="M4 20L18 6M9 15l-3-1M12 12l-3-2M15 9l-2-3M9 15l1 3M12 12l2 3M15 9l3 2"/><circle cx="19" cy="5" r="2"/></svg></div><h2>Memorials</h2><p>You can submit a memorial to your loved and lost pets.</p></article>
<article class="abs card" style="--c:var(--terracotta);left:780px;top:803px"><div class="icon"><svg width="26" height="22" viewBox="0 0 26 22" fill="none" stroke="#fff" stroke-width="1.6"><rect x="3" y="6" width="20" height="13"/><path d="M7 6V3h12v3M8 6v13M13 6v13M18 6v13M3 12h20"/></svg></div><h2>Survey</h2><p>We would love to know what you think of our Hospital.</p></article>

<div class="abs tab">FAST FEEDBACK</div>
<textarea class="abs field" style="left:140px" placeholder="What do you think we do well ?"></textarea>
<textarea class="abs field" style="left:353px" placeholder="What do you think we do well ?"></textarea>
<button class="abs submit">submit</button>
<nav class="abs site-nav">
  <h5>site navigation</h5>
  <div class="cols">
    <div><a href="#">Services</a><a href="#">Staff</a><a href="#">Contact</a><a href="#">Map</a><a href="#">History</a></div>
    <div><a href="#">Appointment</a><a href="#">Survey</a><a href="#">Terms</a><a href="#">Privacy Policy</a></div>
  </div>
</nav>
<div class="abs duck" role="img" aria-label="Brown duck character illustration"></div>
<div class="abs rule"></div>
<footer class="abs bottom">
  <div class="phone"><svg width="14" height="14" viewBox="0 0 29 29"><rect width="29" height="29" rx="6" fill="#b79a85"/><path d="M9 7c1.5-1 2.5-.5 3 1l1 3c.3 1-.5 1.7-1.3 2.2.8 2 2.2 3.5 4.2 4.4.5-.8 1.2-1.6 2.2-1.3l3 1c1.5.5 2 1.5 1 3-1.5 2-3.5 2.5-6 1.2C11.5 19.5 9.5 17 8 13.5 7 11 7.5 8.5 9 7z" fill="#4f2f1d"/></svg>02 65550192</div>
  <div class="social"><span></span><span></span><span></span><span></span></div>
  <div class="copy">© 2017. Marlow Vet Clinic. All Rights Reserved.</div>
</footer>
</body>
</html>
```